New Website for ReBranded Company - CrewBeacon

We have a successful company and website currently but it is a little dated. We have re-branded the company from Harbor Signal Networks to CrewBeacon and have a new logo for the new name. We are looking to build a newer fresher website with the new name. I will need a concept of the home page and one inside page. You can see our current site at https://www.harborsignalnetworks.example and the new site will be https://www.crewbeacon.example .

I also really like the https://www.pathlantern.example/ website. I like ledgerkite.example website. I like the https://skillorbit.example/ website.

See the attached document for layout and some text to use. Use the pictures I attached as opposed to pictures from the old site as much as you can.

Target Market(s)

Business

Industry/Entity Type

Software Service

Number of Pages Required

2 page

Font styles to use
Sans Serif

Requirements
Must have
• Use the colors from my logo. Professional but modern. We want people to feel like our product makes their staff feel safer at work.
Should not have
• Don't use any red or orange (no stop colors).

```html
<!DOCTYPE html>
<html lang="en">
<head>
<meta charset="utf-8">
<title>CrewBeacon – Home</title>
<link href="https://fonts.googleapis.com/css2?family=Bebas+Neue&family=Poppins:wght@400;500;600&display=swap" rel="stylesheet">
<style>
:root{
  --green:#6cb33f;
  --green-dark:#4f9a2a;
  --green-deep:#3d7f1f;
  --green-soft:#e9f4e1;
  --blue:#2f8fdc;
  --blue-dark:#1f74bd;
  --blue-soft:#dbeaf8;
  --ink:#1f2328;
  --muted:#6b7077;
  --line:#e3e8ee;
  --tint:#f2f7fc;
  --white:#ffffff;
}
*{margin:0;padding:0;box-sizing:border-box}
html,body{width:1200px;height:5141px;overflow:hidden;background:var(--white)}
body{font-family:'Poppins',sans-serif;color:var(--ink)}
.page{position:relative;width:1200px;height:5141px;overflow:hidden}
.abs{position:absolute}
.btn{position:absolute;display:flex;align-items:center;justify-content:center;border-radius:22px;color:var(--white);font-size:12.5px;font-weight:500;letter-spacing:.3px;text-transform:uppercase;white-space:nowrap}
.btn-green{background:var(--green)}
.btn-blue{background:var(--blue)}
.center{left:0;width:1200px;text-align:center}
.h2{font-size:29px;font-weight:500;line-height:42px;color:var(--ink)}
.h2 .accent{color:var(--green)}
.brand{display:flex;align-items:center;gap:8px;font-weight:600;color:var(--blue);white-space:nowrap}
.brand .dot{border-radius:50%;background:var(--blue)}
.nav a{position:absolute;top:40px;font-size:12.5px;color:var(--white);text-decoration:none;white-space:nowrap}
.hero-title{left:162px;top:258px;font-family:'Bebas Neue',sans-serif;font-size:56px;line-height:52px;color:var(--green);letter-spacing:.5px}
.hero-sub{left:162px;top:430px;font-size:14.5px;color:#3b3f45}
.round-arrow{position:absolute;width:36px;height:36px;border-radius:50%;display:flex;align-items:center;justify-content:center}
.feature{position:absolute;top:724px;width:240px;text-align:center}
.feature p{margin-top:34px;font-size:12px;line-height:20px;color:var(--muted)}
.photo{position:absolute}
.section-title{font-size:27px;font-weight:500;color:var(--blue);line-height:36px}
.body-text{font-size:12.5px;line-height:22px;color:var(--muted)}
.monitor{position:absolute}
.monitor .frame{position:absolute;left:0;top:0;right:0;border-radius:10px 10px 0 0;background:#2f3438}
.monitor .screen{position:absolute;background:var(--white);padding:10px}
.monitor .chin{position:absolute;left:0;right:0;background:#e6e8ea;border-radius:0 0 10px 10px}
.monitor .neck{position:absolute;background:linear-gradient(#dfe2e5,#f3f4f5)}
.monitor .base{position:absolute;height:8px;background:#dcdfe2;border-radius:4px}
.bar{height:6px;border-radius:3px;background:#e4e7eb;margin-bottom:6px}
.bar.g{background:var(--green-soft)}
.bar.b{background:var(--blue-soft)}
.shield{position:absolute}
.option{position:absolute;width:96px;height:102px;background:var(--white);border-radius:10px;box-shadow:0 3px 12px rgba(40,70,110,.12);display:flex;flex-direction:column;align-items:center;justify-content:center;gap:10px;font-size:12px;color:var(--muted);white-space:nowrap}
.phone-ui{position:absolute;background:var(--white);border:2px solid #dfe3e7;border-radius:30px;box-shadow:0 6px 20px rgba(0,0,0,.08)}
.app-row{position:absolute;left:14px;right:14px;height:30px;border-radius:4px;display:flex;align-items:center;gap:6px;padding:0 6px;font-size:7.5px;font-weight:600;justify-content:space-between;white-space:nowrap}
.app-row .tag{flex:none;font-size:6.5px;font-weight:500;padding:3px 6px;border-radius:2px;white-space:nowrap}
.stat{position:absolute;text-align:center;width:120px}
.stat .num{font-size:48px;font-weight:600;color:var(--green);line-height:52px}
.stat .lbl{font-size:13px;color:#3b3f45}
.stat .pin{width:12px;height:12px;border-radius:50%;border:2px solid var(--blue);margin:10px auto 0;background:var(--white)}
.step{position:absolute;top:4090px;width:300px}
.step .big{position:absolute;left:-56px;top:0;font-size:200px;font-weight:600;line-height:200px;color:#eef4ea}
.step .ic{position:absolute;left:0;top:44px;width:40px;height:40px;border-radius:50%;display:flex;align-items:center;justify-content:center}
.step h4{position:absolute;left:0;top:90px;font-size:14px;font-weight:500;color:var(--blue);line-height:20px;white-space:nowrap}
.step ul{position:absolute;left:0;top:120px;list-style:none;font-size:11.5px;line-height:22px;color:var(--muted)}
.band{position:absolute;left:0;top:4444px;width:1200px;height:342px;background:linear-gradient(120deg,#6fb544 0%,#5ea637 100%)}
.foot-col{position:absolute;top:4830px}
.foot-col h5{font-size:14px;font-weight:500;color:var(--blue);margin-bottom:16px}
.foot-col li{list-style:none;font-size:11px;color:var(--muted);line-height:24px;padding-left:16px;position:relative;white-space:nowrap}
.foot-col li::before{content:"";position:absolute;left:0;top:10px;width:5px;height:5px;border-radius:50%;background:var(--green)}
</style>
</head>
<body>
<div class="page">

  <svg width="0" height="0" style="position:absolute">
    <defs>
      <symbol id="shield" viewBox="0 0 64 72">
        <path d="M32 2 L60 12 V34 C60 52 46 64 32 70 C18 64 4 52 4 34 V12 Z" fill="currentColor"/>
        <path d="M32 8 L54 16 V34 C54 48 43 58 32 63 C21 58 10 48 10 34 V16 Z" fill="none" stroke="#fff" stroke-opacity=".35" stroke-width="1.5"/>
      </symbol>
    </defs>
  </svg>

  <!-- Hero -->
  <svg class="abs" style="left:0;top:0" width="1200" height="620" aria-hidden="true">
    <defs>
      <linearGradient id="heroGreen" x1="0" y1="0" x2="1" y2="1">
        <stop offset="0" stop-color="#7cc24f"/>
        <stop offset="1" stop-color="#4f9a2a"/>
      </linearGradient>
    </defs>
    <path d="M362 0 C420 130 640 210 900 300 C1040 350 1140 420 1200 590 L1200 0 Z" fill="url(#heroGreen)"/>
  </svg>
  <div class="abs" role="img" aria-label="Photo of an office worker pressing a wireless panic button, tinted green" style="left:700px;top:0;width:500px;height:300px;background:linear-gradient(160deg,rgba(255,255,255,.08),rgba(0,0,0,.08))"></div>

  <div class="abs brand" style="left:160px;top:26px;font-size:22px">
    <span class="dot" style="width:26px;height:26px"></span>CrewBeacon
  </div>
  <nav class="nav">
    <a style="left:594px">Home</a>
    <a style="left:654px">Buy Addons</a>
    <a style="left:746px">Cust Log</a>
  </nav>
  <div class="btn btn-blue" style="left:844px;top:28px;width:194px;height:38px">Ready to get started</div>

  <h1 class="abs hero-title">Feel confident<br>that your staff is<br>protected</h1>
  <p class="abs hero-sub">Get a Revolutionary New Electronic Panic Button</p>
  <div class="btn btn-blue" style="left:162px;top:468px;width:222px;height:38px">Ready to get started</div>

  <div class="phone-ui" style="left:732px;top:188px;width:182px;height:382px;border-radius:26px">
    <div class="abs" style="left:72px;top:14px;width:38px;height:4px;border-radius:2px;background:#dfe3e7"></div>
    <div class="abs brand" style="left:30px;top:72px;font-size:14px"><span class="dot" style="width:14px;height:14px"></span>CrewBeacon</div>
    <div class="abs" role="img" aria-label="Photo of a hand holding a panic button fob" style="left:10px;top:128px;width:160px;height:128px;background:linear-gradient(135deg,#55606a,#2d343a)"></div>
    <p class="abs" style="left:10px;top:276px;width:160px;text-align:center;font-size:10.5px;line-height:18px;color:var(--blue)">Get a Revolutionary New Electronic Panic Button</p>
    <div class="abs" style="left:78px;top:338px;width:24px;height:24px;border-radius:50%;border:1.5px solid #dfe3e7"></div>
  </div>
  <div class="round-arrow" style="left:948px;top:518px;background:var(--green)"><svg width="12" height="12" viewBox="0 0 12 12"><path d="M8 2 L4 6 L8 10" stroke="#fff" stroke-width="2" fill="none"/></svg></div>
  <div class="round-arrow" style="left:994px;top:518px;background:var(--blue)"><svg width="12" height="12" viewBox="0 0 12 12"><path d="M4 2 L8 6 L4 10" stroke="#fff" stroke-width="2" fill="none"/></svg></div>

  <svg class="abs" style="left:572px;top:626px" width="56" height="22" aria-hidden="true"><path d="M2 2 L28 20 L54 2" stroke="#e3e8ee" stroke-width="2" fill="none"/></svg>

  <!-- Features -->
  <div class="feature" style="left:236px">
    <svg width="66" height="74" style="color:var(--green)"><use href="#shield"/><rect x="24" y="22" width="16" height="22" rx="2" fill="none" stroke="#fff" stroke-width="2"/><path d="M28 29h8M28 34h8M28 39h5" stroke="#fff" stroke-width="1.6"/></svg>
    <p>Problems Stopped Before They<br>StartFor Any Type Of<br>Organization</p>
  </div>
  <div class="feature" style="left:480px">
    <svg width="66" height="74" style="color:var(--blue)"><use href="#shield"/><path d="M25 44 h16 l-2 -16 h-12 z" fill="none" stroke="#fff" stroke-width="2"/><text x="33" y="41" text-anchor="middle" font-family="Poppins" font-size="11" font-weight="600" fill="#fff">$</text></svg>
    <p>Affordable Prices Starting at $18<br>per month. No Contracts. No<br>Hidden Costs.</p>
  </div>
  <div class="feature" style="left:736px">
    <svg width="66" height="74" style="color:var(--green)"><use href="#shield"/><path d="M24 40 c2-2 2-6 2-10 a7 7 0 0 1 14 0 c0 4 0 8 2 10 z" fill="none" stroke="#fff" stroke-width="2"/><circle cx="33" cy="44" r="2" fill="#fff"/></svg>
    <p>Alerts by computer, Mobile Device,<br>Text, Phone, Email, Monitoringand<br>E911</p>
  </div>

  <!-- Not alone -->
  <h2 class="abs center h2" style="top:970px;font-size:27px;line-height:38px">Your Employess Shouldn't Feel Alone<br>When They Need Help</h2>
  <p class="abs center" style="top:1066px;font-size:12.5px;color:var(--muted)">Does this Problem make you feel frustrated and anxious?</p>
  <p class="abs center" style="top:1092px;font-size:14px;color:var(--blue)">Put a simple solution in their hands</p>
  <div class="btn btn-green" style="left:490px;top:1134px;width:220px;height:38px">Ready to get started</div>
  <div class="photo" role="img" aria-label="Photo of a business team standing behind a desk phone fitted with a panic button" style="left:296px;top:1180px;width:610px;height:370px;background:linear-gradient(180deg,#eef1f4 0%,#d8dde2 55%,#3a3f45 100%);border-radius:4px 4px 0 0"></div>
  <div class="abs" style="left:232px;top:1548px;width:736px;height:4px;background:var(--blue)"></div>
  <div class="round-arrow" style="left:238px;top:1488px;width:32px;height:32px;background:var(--green)"><svg width="12" height="12" viewBox="0 0 12 12"><path d="M8 2 L4 6 L8 10" stroke="#fff" stroke-width="2" fill="none"/></svg></div>
  <div class="round-arrow" style="left:928px;top:1488px;width:32px;height:32px;background:var(--green)"><svg width="12" height="12" viewBox="0 0 12 12"><path d="M4 2 L8 6 L4 10" stroke="#fff" stroke-width="2" fill="none"/></svg></div>

  <!-- Why -->
  <h2 class="abs center h2" style="top:1694px">Why Businesses <span class="accent">Choose Us</span></h2>

  <svg class="abs" style="left:0;top:1780px" width="1200" height="1600" aria-hidden="true">
    <polygon points="0,200 1200,40 1200,1420 0,1580" fill="var(--tint)"/>
    <polygon points="0,420 1200,330 1200,380 0,470" fill="#ffffff" opacity=".7"/>
  </svg>

  <!-- Easy to use -->
  <div class="monitor" style="left:208px;top:1816px;width:374px;height:310px">
    <div class="frame" style="height:232px"></div>
    <div class="screen" style="left:62px;top:8px;width:250px;height:222px">
      <div class="bar" style="width:60%"></div>
      <div style="display:flex;gap:10px;margin-top:10px">
        <div style="width:80px"><div class="bar" style="width:70%"></div><div class="bar b" style="width:50%"></div><div class="bar"></div><div class="bar" style="width:80%"></div><div class="bar" style="width:60%"></div></div>
        <div style="flex:1"><div class="bar g"></div><div class="bar g" style="width:80%"></div><div class="bar g"></div><div class="bar" style="width:60%"></div><div class="bar b" style="width:70%;margin-left:30%"></div><div class="bar" style="width:50%"></div></div>
      </div>
    </div>
    <div class="chin" style="top:232px;height:22px"></div>
    <div class="neck" style="left:152px;top:254px;width:70px;height:40px"></div>
    <div class="base" style="left:132px;top:292px;width:110px"></div>
  </div>
  <svg class="shield" style="left:546px;top:1886px;color:var(--green)" width="76" height="86"><use href="#shield" width="76" height="86"/><path d="M30 52 l18 -22 M30 34 l16 16" stroke="#fff" stroke-width="2.4"/></svg>
  <h3 class="abs section-title" style="left:692px;top:1886px">Easy To Use</h3>
  <p class="abs body-text" style="left:690px;top:1932px;width:310px">Press a button and let the right people know you need help and open a chat window letting everyone talk on resolving their problem.</p>

  <!-- Community -->
  <h3 class="abs section-title" style="left:202px;top:2228px">Community The Way<br>You Want</h3>
  <p class="abs" style="left:202px;top:2308px;font-size:12px;color:#3b3f45">We Give You Lots of Options :</p>

  <div class="option" style="left:200px;top:2360px"><svg width="44" height="36" viewBox="0 0 44 36" fill="none" stroke="#333" stroke-width="2"><rect x="2" y="2" width="40" height="24" rx="2" fill="var(--green-soft)"/><path d="M16 34h12M22 26v8"/></svg>Computer</div>
  <div class="option" style="left:314px;top:2376px"><svg width="26" height="40" viewBox="0 0 26 40" fill="none" stroke="#333" stroke-width="2"><rect x="2" y="2" width="22" height="36" rx="3" fill="var(--green-soft)"/><circle cx="13" cy="32" r="2"/></svg>Mobile</div>
  <div class="option" style="left:426px;top:2360px"><svg width="44" height="38" viewBox="0 0 44 38" fill="none" stroke="#333" stroke-width="2"><path d="M2 2h40v24H14l-8 8v-8H2z" fill="var(--green-soft)"/><path d="M10 10h24M10 17h18"/></svg>Text</div>
  <div class="option" style="left:200px;top:2480px"><svg width="44" height="32" viewBox="0 0 44 32" fill="none" stroke="#333" stroke-width="2"><rect x="2" y="2" width="40" height="28" rx="2" fill="var(--green-soft)"/><path d="M2 2l20 16L42 2"/></svg>Email</div>
  <div class="option" style="left:314px;top:2494px"><svg width="40" height="38" viewBox="0 0 40 38" fill="none" stroke="#333" stroke-width="2"><rect x="10" y="2" width="20" height="10"/><rect x="2" y="12" width="36" height="16" rx="2" fill="var(--green-soft)"/><rect x="10" y="24" width="20" height="12"/></svg>E911</div>
  <div class="option" style="left:426px;top:2480px"><svg width="40" height="40" viewBox="0 0 40 40" fill="none" stroke="#333" stroke-width="2"><circle cx="20" cy="18" r="10" fill="var(--green-soft)"/><path d="M6 20a14 14 0 0 1 28 0M8 20v6M32 20v6q0 8-10 8"/></svg>Call Center</div>
  <div class="option" style="left:314px;top:2606px"><svg width="40" height="40" viewBox="0 0 40 40" fill="none" stroke="#333" stroke-width="2"><path d="M10 4l6 8-4 4q4 8 12 12l4-4 8 6-4 6Q14 36 4 10z" fill="var(--green-soft)"/><path d="M24 6a10 10 0 0 1 10 10M24 12a4 4 0 0 1 4 4"/></svg>Phone Call</div>

  <div class="phone-ui" style="left:726px;top:2250px;width:214px;height:450px">
    <div class="abs" style="left:70px;top:20px;width:70px;height:6px;border-radius:3px;background:#e3e8ee"></div>
    <p class="abs" style="left:20px;top:48px;font-size:8px;font-weight:600">9:32</p>
    <div class="abs" style="left:18px;top:66px;width:12px;height:12px;border-radius:50%;background:var(--green-dark)"></div>
    <p class="abs" style="left:36px;top:66px;font-size:8px;font-weight:500">HARLOW WORKS</p>
    <div class="abs" style="left:18px;top:104px;width:176px;height:14px;border-radius:3px;background:#f1f3f5"></div>
    <div class="app-row" style="top:130px;background:#fff;border:1px solid var(--line)"><span>▲ INTERNET DOWN</span><span class="tag" style="background:var(--green-soft);color:var(--green-deep)">Raise alert</span></div>
    <div class="app-row" style="top:166px;background:#fff;border:1px solid var(--line)"><span>▲ MAINTENANCE</span><span class="tag" style="background:var(--blue);color:#fff">Raise alert</span></div>
    <div class="app-row" style="top:290px;background:var(--blue);color:#fff"><span>I NEED ASSISTANCE</span><span class="tag" style="background:#fff;color:#333">Raise alert</span></div>
    <div class="app-row" style="top:326px;background:var(--green-dark);color:#fff"><span>EMERGENCY</span><span class="tag" style="background:#fff;color:#333">Raise alert</span></div>
    <div class="abs" style="left:18px;top:370px;width:176px;height:1px;background:var(--line)"></div>
    <div class="abs" style="left:90px;top:410px;width:30px;height:30px;border-radius:50%;border:1.5px solid #dfe3e7"></div>
  </div>
  <svg class="shield" style="left:682px;top:2440px;color:var(--green)" width="76" height="86"><use href="#shield" width="76" height="86"/><circle cx="30" cy="38" r="5" fill="none" stroke="#fff" stroke-width="2"/><circle cx="46" cy="38" r="5" fill="none" stroke="#fff" stroke-width="2"/><path d="M22 54q8-10 16 0q8-10 16 0" fill="none" stroke="#fff" stroke-width="2"/></svg>

  <!-- Cost -->
  <div class="monitor" style="left:212px;top:2816px;width:374px;height:334px">
    <div class="frame" style="height:254px"></div>
    <div class="screen" style="left:52px;top:8px;width:270px;height:244px">
      <div class="bar" style="width:60%"></div>
      <div style="display:flex;gap:10px;margin-top:10px">
        <div style="width:80px"><div style="height:40px;border-radius:3px;background:var(--green-dark);margin-bottom:6px"></div><div style="height:40px;border-radius:3px;background:var(--blue)"></div></div>
        <div style="flex:1"><div class="bar" style="width:40%"></div><div class="bar b" style="width:80%"></div><div style="height:50px"></div><div class="bar" style="width:40%"></div><div class="bar b" style="width:80%"></div></div>
      </div>
    </div>
    <div class="chin" style="top:254px;height:22px"></div>
    <div class="neck" style="left:152px;top:276px;width:70px;height:42px"></div>
    <div class="base" style="left:132px;top:316px;width:110px"></div>
  </div>
  <svg class="shield" style="left:546px;top:2886px;color:var(--green)" width="76" height="86"><use href="#shield" width="76" height="86"/><path d="M24 52h28M28 52V40M36 52V34M44 52V28" stroke="#fff" stroke-width="2.4"/></svg>
  <h3 class="abs section-title" style="left:688px;top:2866px">Cost Effective<br>Protection</h3>
  <p class="abs body-text" style="left:688px;top:2950px;width:320px">By leveraging your existing network and equipment we can lower your costs to give better options to your staff.</p>
  <div class="btn btn-green" style="left:690px;top:3034px;width:222px;height:38px">Ready to get started</div>

  <!-- Scary -->
  <h2 class="abs center h2" style="top:3340px">We Know How Scary it Can Feel to<br>Worry About <span class="accent">Employee Safety.</span></h2>
  <p class="abs center" style="top:3444px;font-size:12.5px;line-height:24px;color:var(--blue)">That's why we have provided a way for customers to get<br>help to staff effectively in</p>
  <div class="photo" role="img" aria-label="Faint dotted world map" style="left:300px;top:3500px;width:600px;height:420px;background:radial-gradient(ellipse at center,#eef2f6 0%,#ffffff 70%)"></div>
  <div class="stat" style="left:400px;top:3512px"><div class="num">45</div><div class="lbl">States</div><div class="pin"></div></div>
  <p class="abs" style="left:560px;top:3532px;width:80px;text-align:center;font-size:14px;color:#3b3f45;border-bottom:2px solid var(--blue);padding-bottom:2px">Covering</p>
  <div class="stat" style="left:670px;top:3512px"><div class="num">5</div><div class="lbl">Countries</div><div class="pin"></div></div>
  <div class="photo" role="img" aria-label="Photo of a smiling support agent wearing a headset" style="left:500px;top:3630px;width:200px;height:290px;background:linear-gradient(180deg,#e6e2dd 0%,#c9c3bc 60%,#9fb7d0 100%);border-radius:100px 100px 0 0"></div>
  <div class="abs" style="left:232px;top:3918px;width:736px;height:4px;background:var(--blue)"></div>
  <div class="btn btn-green" style="left:490px;top:3902px;width:220px;height:38px">Ready to get started</div>

  <!-- Plan -->
  <h2 class="abs center h2" style="top:4016px">Simple Start <span class="accent">Plan</span></h2>
  <div class="step" style="left:226px">
    <div class="big">1</div>
    <div class="ic" style="left:0;background:var(--green)"><svg width="20" height="20" viewBox="0 0 20 20" fill="none" stroke="#fff" stroke-width="2"><circle cx="10" cy="10" r="7"/><path d="M10 6v4l3 2"/></svg></div>
    <h4>Explore Your Choices</h4>
    <ul><li>Pricing</li><li>Trial</li><li>Quote</li><li>Hardware</li></ul>
  </div>
  <div class="step" style="left:530px">
    <div class="big">2</div>
    <div class="ic" style="background:var(--blue)"><svg width="20" height="20" viewBox="0 0 20 20" fill="none" stroke="#fff" stroke-width="2"><circle cx="10" cy="10" r="3"/><circle cx="10" cy="10" r="7" stroke-dasharray="3 2"/></svg></div>
    <h4>Get Set Up</h4>
    <ul><li>Input Your Alerts</li><li>Input Your Staff</li><li>Install Our Software</li></ul>
  </div>
  <div class="step" style="left:840px">
    <div class="big">3</div>
    <div class="ic" style="background:var(--green)"><svg width="20" height="20" viewBox="0 0 20 20" fill="none" stroke="#fff" stroke-width="2"><path d="M5 10l3 3 7-7"/></svg></div>
    <h4>Feel Confident Your<br>Staff Is Protected</h4>
    <ul style="top:140px;width:200px"><li style="line-height:21px">High Five. You just too a major step to getting rid of the anxiety &amp; frustration this gave you.</li></ul>
  </div>
  <div class="btn btn-green" style="left:490px;top:4324px;width:220px;height:38px">Ready to get started</div>

  <!-- Band -->
  <div class="band" role="img" aria-label="Green-tinted photo of an office desk"></div>
  <svg class="abs" style="left:570px;top:4496px;color:rgba(255,255,255,.2)" width="60" height="68"><use href="#shield" width="60" height="68"/><path d="M22 30a12 12 0 0 1 16 0M26 35a6 6 0 0 1 8 0" stroke="#fff" stroke-width="2" fill="none"/><circle cx="30" cy="40" r="2" fill="#fff"/></svg>
  <h2 class="abs center" style="top:4578px;font-size:29px;font-weight:500;line-height:42px;color:var(--white)">Stay Connected with Staff Duringa<br>Crisis Situations</h2>
  <div class="btn btn-blue" style="left:490px;top:4678px;width:220px;height:38px">Ready to get started</div>

  <!-- Footer -->
  <div class="abs brand" style="left:160px;top:4838px;font-size:30px"><span class="dot" style="width:34px;height:34px"></span>CrewBeacon</div>
  <p class="abs" style="left:162px;top:4912px;width:260px;font-size:11px;line-height:22px;color:var(--muted)">When employees feel alone during a threatening situation, we give them a way to let the right resources knowthat they need help so you can feel confident that your staff is protected.</p>
  <div class="abs" style="left:160px;top:5034px;display:flex;align-items:center;gap:10px;color:var(--green);font-size:20px;font-weight:600;white-space:nowrap">
    <svg width="30" height="30" viewBox="0 0 30 30" fill="none" stroke="var(--green)" stroke-width="2"><circle cx="15" cy="15" r="13"/><path d="M10 8l3 4-2 2q2 4 6 6l2-2 4 3-2 3q-10-2-13-13z"/></svg>1.800.555.0148
  </div>

  <div class="foot-col" style="left:486px"><h5>Shop</h5><ul><li>Add ons</li><li>Start My Demo</li><li>Custom Quote</li><li>Start Trial</li></ul></div>
  <div class="foot-col" style="left:676px"><h5>About</h5><ul><li>Affiliates</li><li>Contact</li><li>Support</li><li>Existing Customers</li><li>Industries</li><li>Blog</li><li>Faq's</li></ul></div>
  <div class="foot-col" style="left:866px"><h5>Legal</h5><ul><li>Privacy Policy</li><li>Terms of Use</li><li>End User License Agreement</li></ul></div>

  <p class="abs center" style="top:5116px;font-size:10.5px;color:var(--muted)">©CrewBeacon 2020 All rights reserved</p>
</div>
</body>
</html>
```